Radiant Harvest Gathering 2021

I am looking to create a flyer for a one day prayer retreat our church is organizing. This flyer will be posted on social media, websites, mobile apps, and will also be printed so it can be mailed to people.

I am looking for something professional, with good use of our logo and band colors (logo colors).

I am counting on the designer's skill, creativity, art and knowledge of media communication to produce a flyer that will effectively and quickly convey the message we are trying to spread.

CONTENT OF THE FLYER:
Event title: Radiant Harvest Gathering
Date: Tuesday July 2nd, 2021
Time: 11:00AM - 7:00PM
Bellmore Hotel, 4817 Wexley Avenue, Portland, Maine 04109 (Room: Tamarind)
Event Key words to highlight what the event is about: Prayer, Fasting, Worship, Prophecy, Revival.
Key phrases:
A one day prayer retreat.
Jesus Chris is Lord

Contact info:
www.quvello.org
Phone: 207 555 0148
Email: contact@brookmeadow.org

```html
<!DOCTYPE html>
<html lang="en">
<head>
<meta charset="utf-8">
<title>Radiant Harvest Gathering 2021</title>
<link rel="stylesheet" href="https://fonts.googleapis.com/css2?family=Bebas+Neue&family=Montserrat:wght@500;600&display=swap">
<style>
  :root {
    --page: #efe6d4;
    --flyer: #000000;
    --white: #ffffff;
    --orange: #f08c1c;
    --navy: #1b2f5a;
    --grey-dark: #1a1a1a;
    --grey-mid: #6d6d6d;
  }
  * { margin: 0; padding: 0; box-sizing: border-box; }
  html, body {
    width: 1200px; height: 659px; overflow: hidden;
    background: var(--page);
    font-family: "Montserrat", sans-serif;
  }
  .flyer {
    position: absolute; left: 360px; top: 20px;
    width: 480px; height: 619px;
    background: var(--flyer); color: var(--white);
    overflow: hidden;
  }
  .hero-photo {
    position: absolute; left: 0; top: 0; width: 236px; height: 385px;
    background: radial-gradient(ellipse at 55% 40%, #b9b9b9 0%, var(--grey-mid) 30%, var(--grey-dark) 65%, var(--flyer) 100%);
  }
  .title { position: absolute; left: 236px; top: 33px; width: 226px; height: 368px; }
  .title text { font-family: "Bebas Neue", sans-serif; }

  .key-phrases {
    position: absolute; left: 12px; top: 394px; width: 206px; height: 63px;
    border: 1.5px solid var(--white);
    text-align: center; font-size: 12.5px; font-weight: 500;
  }
  .key-phrases .label {
    position: absolute; top: -7px; left: 50%; transform: translateX(-50%);
    background: var(--flyer); padding: 0 5px;
    color: var(--orange); font-size: 9.5px; font-weight: 600; white-space: nowrap;
  }
  .key-phrases .phrase { margin-top: 10px; }
  .key-phrases .rule { width: 34px; height: 1px; background: var(--orange); margin: 6px auto 5px; }

  .brand { position: absolute; left: 20px; top: 502px; display: flex; align-items: center; gap: 8px; }
  .brand-dot { width: 14px; height: 14px; border-radius: 50%; background: var(--orange); }
  .brand-name { font-size: 26px; font-weight: 600; color: var(--white); letter-spacing: 1px; }

  .contact { position: absolute; left: 20px; top: 556px; font-size: 12px; font-weight: 600; line-height: 16px; }
  .contact li { list-style: none; display: flex; align-items: center; gap: 6px; white-space: nowrap; }
  .contact svg { width: 9px; height: 9px; flex: none; }

  .divider-v { position: absolute; left: 218px; top: 479px; width: 1px; height: 124px; background: var(--white); }
  .rule-orange { position: absolute; left: 233px; width: 230px; height: 1.5px; background: var(--orange); }

  .venue { position: absolute; left: 233px; top: 431px; display: flex; gap: 10px; }
  .venue svg { width: 48px; height: 50px; flex: none; margin-top: 2px; }
  .venue address { font-style: normal; font-size: 12.8px; font-weight: 500; line-height: 15.5px; }
  .venue .room { color: var(--orange); font-size: 11.5px; }

  .program { position: absolute; left: 237px; top: 506px; }
  .program h2 { color: var(--orange); font-size: 16.5px; font-weight: 600; line-height: 20px; margin-bottom: 6px; }
  .program ul { display: grid; grid-template-columns: 112px 110px; row-gap: 6px; list-style: none; }
  .program li { display: flex; align-items: center; gap: 5px; font-size: 14px; font-weight: 500; line-height: 17px; }
  .program svg { width: 17px; height: 17px; flex: none; }
</style>
</head>
<body>
  <main class="flyer">
    <div class="hero-photo" role="img" aria-label="Black and white photo of clasped praying hands holding a cross on a chain"></div>

    <svg class="title" viewBox="0 0 224 390" preserveAspectRatio="none" aria-label="Radiant Harvest Gathering, Tuesday July 2nd 2021, 11:00AM to 7:00PM">
      <text x="0" y="62" font-size="88" fill="var(--white)" textLength="224" lengthAdjust="spacingAndGlyphs">RADIANT</text>
      <text x="0" y="166" font-size="140" fill="var(--white)" textLength="224" lengthAdjust="spacingAndGlyphs">HARVEST</text>
      <text x="0" y="250" font-size="110" fill="var(--orange)" textLength="224" lengthAdjust="spacingAndGlyphs">GATHERING</text>
      <rect x="0" y="260" width="224" height="130" fill="var(--white)"/>
      <text x="7" y="303" font-size="54" fill="var(--navy)" textLength="210" lengthAdjust="spacingAndGlyphs">TUESDAY</text>
      <text x="7" y="333" font-size="34" fill="var(--orange)" textLength="210" lengthAdjust="spacingAndGlyphs">JULY 2ND, 2021</text>
      <text x="7" y="382" font-size="58" fill="var(--navy)" textLength="210" lengthAdjust="spacingAndGlyphs">11:00AM - 7:00PM</text>
    </svg>

    <section class="key-phrases">
      <span class="label">KEY PHRASES:</span>
      <p class="phrase">A one day prayer retreat.</p>
      <div class="rule"></div>
      <p>Jesus Chris is Lord</p>
    </section>

    <div class="brand">
      <span class="brand-dot"></span>
      <span class="brand-name">QUVELLO</span>
    </div>

    <ul class="contact">
      <li><svg viewBox="0 0 10 10"><circle cx="5" cy="5" r="5" fill="var(--orange)"/></svg>207 555 0148</li>
      <li><svg viewBox="0 0 10 10"><circle cx="5" cy="5" r="5" fill="var(--orange)"/></svg>www.quvello.org</li>
      <li><svg viewBox="0 0 10 10"><circle cx="5" cy="5" r="5" fill="var(--orange)"/></svg>contact@brookmeadow.org</li>
    </ul>

    <div class="divider-v"></div>
    <div class="rule-orange" style="top:416px"></div>

    <div class="venue">
      <svg viewBox="0 0 48 50" aria-hidden="true">
        <ellipse cx="24" cy="41" rx="21" ry="6" fill="none" stroke="var(--orange)" stroke-width="3"/>
        <path d="M24 41 C14 28 10 22 10 15 A14 14 0 0 1 38 15 C38 22 34 28 24 41Z" fill="var(--orange)"/>
        <circle cx="24" cy="15" r="5.5" fill="var(--flyer)"/>
      </svg>
      <address>
        Bellmore Hotel,<br>
        4817 Wexley Avenue,<br>
        Portland, Maine 04109<br>
        <span class="room">(Room: Tamarind)</span>
      </address>
    </div>

    <div class="rule-orange" style="top:498px"></div>

    <section class="program">
      <h2>Event Program:</h2>
      <ul>
        <li><svg viewBox="0 0 20 20"><circle cx="10" cy="10" r="10" fill="var(--orange)"/><path d="M5.5 10.5 L8.7 13.5 L14.5 7" fill="none" stroke="var(--white)" stroke-width="2.4"/></svg>PRAYER</li>
        <li><svg viewBox="0 0 20 20"><circle cx="10" cy="10" r="10" fill="var(--orange)"/><path d="M5.5 10.5 L8.7 13.5 L14.5 7" fill="none" stroke="var(--white)" stroke-width="2.4"/></svg>FASTING</li>
        <li><svg viewBox="0 0 20 20"><circle cx="10" cy="10" r="10" fill="var(--orange)"/><path d="M5.5 10.5 L8.7 13.5 L14.5 7" fill="none" stroke="var(--white)" stroke-width="2.4"/></svg>WORSHIP</li>
        <li><svg viewBox="0 0 20 20"><circle cx="10" cy="10" r="10" fill="var(--orange)"/><path d="M5.5 10.5 L8.7 13.5 L14.5 7" fill="none" stroke="var(--white)" stroke-width="2.4"/></svg>PROPHECY</li>
        <li><svg viewBox="0 0 20 20"><circle cx="10" cy="10" r="10" fill="var(--orange)"/><path d="M5.5 10.5 L8.7 13.5 L14.5 7" fill="none" stroke="var(--white)" stroke-width="2.4"/></svg>REVIVAL</li>
      </ul>
    </section>
  </main>
</body>
</html>
```